Business Consulting Website Design

UPDATED KEY MESSAGES:

The client has decided o a different direction.

The Key Messages include:
-- Creating something unique.
Every company is unique, ever culture unique. Every project customized to meet the unique needs of the client. No two things are alike.
-- One of a kind
Because every company is different, every culture is different, every objective is unique
-- Customized solutions
We create something just for you …

I think the approach needs to be about creating a masterpiece as opposed to nurturing/growing.

Perhaps we could have different abstract/colorful paint items that takes up part of the page for each landing page. Against white and on the white is where we put our text.

Client also has created a Pixelgrove Lightbox with images that she likes

http://www.pixelgrove-example.com/public_board.mhtml?code=a7c2e9f04b8d13562e7f90a1c4d6b852&board_id=58217409

She also likes the watercolor look against white background.

===============================
Need a Homepage and an Interior page redesign for my client: http://www.brightwavecounsel-example.com

Client does leadership development, performance management, talent development, etc. Has some great clients.

- This site is very old and needs a modern look. Update look & colors. She wants simple but not bland.
- Banner images should be interesting.
- She likes the purple in her logo
- She thinks Arial font is outdated and boring
- We will be rewriting all the copy.
- Design should include ProLinker icon, phone, email, and address
- She likes the client grid on the Our Clients page. We will be redoing this.

- Menus will include:
-- Home
-- What We Do
-- Who We Are
-- Our Clients
-- Snapshots (these are case studies)

One of the sites she liked is http://lanternfold-novel-example.com, though this website has much more content than she will have.

I'm attaching the following files for your reference:
- Her new business card proof that contains her logo
- a zip file containing some stock image comps

Need strong design. Site will likely be built in Wordpress.

Thanks,
Nora
Updates

Target Market(s)

SVP of Human Resources or Head of Talent

Industry/Entity Type

Business

Number of Pages Required

2 page

Font styles to use
Sans Serif

Colors
b768aa
876aae
6b449b
f04a50
f37122

Requirements
Must have
• - Designer must read the brief
• - Use logo
Nice to have
• - Strong banner images to complement the key message
• - Design will function work on mobile easily
Should not have
• - Should not look like a design template was purchased from layoutbazaar-example.com or other template sites.
• - Should not be too masculine
• - Should not feel cluttered.

```html
<!DOCTYPE html>
<html lang="en">
<head>
<meta charset="utf-8">
<title>Brightwave Counsel — Human Resource Communications</title>
<link href="https://fonts.googleapis.com/css2?family=Open+Sans:wght@300;400;600;700&display=swap" rel="stylesheet">
<style>
  :root{
    --purple:#6b449b;
    --purple-soft:#876aae;
    --orchid:#b768aa;
    --orange:#f37122;
    --amber:#f4a04a;
    --coral:#f04a50;
    --ink:#4a4a4a;
    --muted:#8a8a8a;
    --line:#dcdcdc;
    --paper:#ffffff;
    --mist:#f1f1f1;
    --strip:#e9e9e9;
    --footer:#2c2c2c;
    --footer-deep:#202020;
  }
  *{box-sizing:border-box;margin:0;padding:0}
  html,body{width:681px;height:1200px;overflow:hidden}
  body{font-family:"Open Sans",Arial,sans-serif;color:var(--ink);background:var(--paper);position:relative}

  /* Hero: watercolour paint on white */
  .hero{position:absolute;left:0;top:0;width:681px;height:295px;overflow:hidden;background:var(--paper)}
  .hero-paint{position:absolute;left:300px;top:20px;width:400px;height:290px;border-radius:48% 52% 40% 60% / 55% 45% 55% 45%;
    background:radial-gradient(ellipse at 35% 40%,rgba(183,104,170,.85) 0%,rgba(135,106,174,.7) 30%,rgba(240,74,80,.45) 55%,rgba(243,113,34,.3) 72%,rgba(255,255,255,0) 88%)}
  .brand{position:absolute;left:68px;top:22px;display:flex;align-items:center;gap:8px}
  .brand-mark{width:18px;height:18px;background:var(--purple)}
  .brand-name{font-size:11px;font-weight:700;letter-spacing:1.5px;color:var(--purple);line-height:1.2;width:90px}
  .main-nav{position:absolute;right:40px;top:13px;display:flex;gap:22px}
  .main-nav a{font-size:7.5px;font-weight:600;color:var(--ink);text-decoration:none;letter-spacing:.5px}
  .main-nav a.active{color:var(--purple);border-bottom:1px solid var(--purple);padding-bottom:2px}
  .hero-title{position:absolute;left:68px;top:138px}
  .hero-title h1{font-size:26px;font-weight:600;line-height:1.1;color:var(--purple)}
  .hero-title p{font-size:16px;font-weight:300;letter-spacing:1px;margin-top:3px;color:var(--orchid)}

  /* What we do */
  .what-we-do{position:absolute;left:0;top:295px;width:681px;height:165px;background:var(--paper);overflow:hidden;border-top:1px solid var(--mist)}
  .accent-tri{position:absolute;left:0;top:0}
  .founder-photo{position:absolute;left:72px;top:14px;width:90px;height:151px;
    background:linear-gradient(180deg,#e8d7c6 0%,#c9a583 45%,#3d3a45 100%);border-radius:45px 45px 0 0}
  .wwd-copy{position:absolute;left:215px;top:14px;width:400px}
  .section-title{font-weight:300;color:var(--purple);letter-spacing:1px}
  .wwd-copy h2{font-size:22px}
  .wwd-copy p{font-size:8.5px;line-height:1.55;color:var(--muted);margin-top:6px}
  .values{position:absolute;left:205px;top:92px;display:flex}
  .value{width:100px;text-align:center}
  .value svg{display:block;margin:0 auto}
  .value span{display:block;font-size:7.5px;color:var(--ink);margin-top:6px}

  /* Services */
  .services{position:absolute;left:0;top:460px;width:681px;height:267px;background:var(--mist)}
  .services h2{text-align:center;font-size:21px;margin-top:20px}
  .service-grid{position:absolute;left:75px;top:80px;display:grid;grid-template-columns:repeat(4,118px);column-gap:18px;row-gap:15px}
  .service-card{height:73px;background:var(--paper);border:1px solid var(--line);display:flex;flex-direction:column;align-items:center;padding-top:12px}
  .service-card.highlight{border:1.5px solid var(--purple-soft)}
  .service-card span{font-size:6.5px;font-weight:600;color:var(--ink);text-align:center;line-height:1.35;margin-top:7px;padding:0 6px;text-transform:uppercase}

  /* Testimonials */
  .testimonials{position:absolute;left:0;top:727px;width:681px;height:273px;overflow:hidden}
  .testimonial-photo{position:absolute;inset:0;
    background:radial-gradient(ellipse at 28% 55%,#5a4a3a 0%,#33302a 35%,#1c1b19 100%)}
  .testimonials h2{position:relative;text-align:center;font-size:21px;color:#fff;margin-top:28px}
  .quote-slider{position:absolute;left:0;right:0;top:92px;display:flex;justify-content:center;align-items:center;gap:8px}
  .slide-arrow{width:18px;height:18px;background:rgba(255,255,255,.85);display:flex;align-items:center;justify-content:center}
  .client-badge{width:62px;height:44px;background:#fff;display:flex;align-items:center;justify-content:center;font-size:9px;font-weight:700;color:var(--coral)}
  .quote-author{position:absolute;left:0;right:0;top:150px;text-align:center;color:#fff}
  .quote-author strong{display:block;font-size:9px;font-weight:600}
  .quote-author em{display:block;font-style:normal;font-size:6.5px;color:#cfcfcf;margin-top:2px}
  .quote-text{position:absolute;left:110px;right:110px;top:184px;text-align:center;color:#e6e6e6;font-size:7px;line-height:1.6}
  .quote-text b{color:var(--amber);font-weight:600}

  /* Client strip */
  .client-strip{position:absolute;left:0;top:1000px;width:681px;height:68px;background:var(--strip);display:flex;align-items:center;justify-content:center;gap:30px}
  .client-strip .edge{position:absolute;top:26px}
  .client-strip .edge.left{left:14px}
  .client-strip .edge.right{right:14px}
  .client-name{font-size:13px;font-weight:700;color:#a9a9a9;white-space:nowrap}

  /* Footer */
  .site-footer{position:absolute;left:0;top:1068px;width:681px;height:132px;background:var(--footer);color:#ddd}
  .site-footer h3{text-align:center;font-size:10px;font-weight:400;letter-spacing:1px;color:#fff;margin-top:16px}
  .contact-row{position:absolute;left:90px;right:60px;top:42px;display:flex;align-items:flex-start}
  .contact-item{display:flex;gap:7px;font-size:6.5px;line-height:1.5;color:#bbb}
  .contact-item strong{display:block;font-size:7.5px;color:#fff;font-weight:600}
  .contact-item.address{width:180px}
  .contact-item.phone{width:140px}
  .contact-item.email{width:160px}
  .social{display:flex;align-items:center;gap:5px;font-size:7px;color:#fff;margin-left:auto;margin-top:4px}
  .social i{width:18px;height:18px;border:1px solid #aaa;border-radius:50%;display:block}
  .footer-bar{position:absolute;left:0;right:0;bottom:0;height:22px;background:var(--footer-deep);display:flex;align-items:center;justify-content:space-between;padding:0 60px 0 90px;font-size:6px;color:#999}
  .footer-bar nav{display:flex;gap:12px}
  .footer-bar a{color:#999;text-decoration:none}
</style>
</head>
<body>

<header class="hero">
  <div class="hero-paint" role="img" aria-label="Abstract watercolour paint wash in purple, orchid, coral and orange on white"></div>
  <div class="brand">
    <div class="brand-mark"></div>
    <div class="brand-name">BRIGHTWAVE COUNSEL</div>
  </div>
  <nav class="main-nav">
    <a href="#" class="active">HOME</a>
    <a href="#">WHAT WE DO</a>
    <a href="#">WHO WE ARE</a>
    <a href="#">OUR CLIENTS</a>
    <a href="#">SNAPSHOTS</a>
  </nav>
  <div class="hero-title">
    <h1>Human Resource</h1>
    <p>COMMUNICATIONS</p>
  </div>
</header>

<section class="what-we-do">
  <svg class="accent-tri" width="120" height="165" viewBox="0 0 120 165">
    <polygon points="0,0 110,0 0,150" fill="#6b449b"/>
    <polygon points="0,0 60,0 0,80" fill="#876aae"/>
  </svg>
  <div class="founder-photo" role="img" aria-label="Portrait of the firm's founder"></div>
  <div class="wwd-copy">
    <h2 class="section-title">WHAT WE DO</h2>
    <p>Brightwave Counsel is a human resource consulting firm with proven experience in developing and implementing programs that help people and teams do their best work.</p>
  </div>
  <div class="values">
    <div class="value">
      <svg width="24" height="24" viewBox="0 0 24 24"><rect x="5" y="5" width="14" height="14" transform="rotate(45 12 12)" fill="#f4a04a"/><path d="M9 12l2 2 4-4" stroke="#fff" stroke-width="1.5" fill="none"/></svg>
      <span>Experience counts</span>
    </div>
    <div class="value">
      <svg width="24" height="24" viewBox="0 0 24 24"><rect x="5" y="5" width="14" height="14" transform="rotate(45 12 12)" fill="#f4a04a"/><circle cx="12" cy="12" r="3.5" stroke="#fff" stroke-width="1.2" fill="none"/><path d="M12 10v2h1.5" stroke="#fff" stroke-width="1" fill="none"/></svg>
      <span>On time. On budget.</span>
    </div>
    <div class="value">
      <svg width="24" height="24" viewBox="0 0 24 24"><rect x="5" y="5" width="14" height="14" transform="rotate(45 12 12)" fill="#f4a04a"/><polygon points="12,8.5 13,11 15.5,11 13.5,12.6 14.3,15 12,13.5 9.7,15 10.5,12.6 8.5,11 11,11" fill="#fff"/></svg>
      <span>Exceptional service</span>
    </div>
    <div class="value">
      <svg width="24" height="24" viewBox="0 0 24 24"><rect x="5" y="5" width="14" height="14" transform="rotate(45 12 12)" fill="#f4a04a"/><circle cx="12" cy="10.5" r="1.8" fill="#fff"/><path d="M9 15c0-2 6-2 6 0" fill="#fff"/></svg>
      <span>Your resource</span>
    </div>
  </div>
</section>

<section class="services">
  <h2 class="section-title">OUR SERVICES</h2>
  <div class="service-grid">
    <div class="service-card highlight">
      <svg width="22" height="22" viewBox="0 0 22 22"><rect x="5" y="3" width="12" height="16" fill="none" stroke="#6b449b" stroke-width="1.2"/><path d="M8 8h6M8 11h6M8 14h4" stroke="#6b449b"/></svg>
      <span>Employee Handbooks</span>
    </div>
    <div class="service-card">
      <svg width="22" height="22" viewBox="0 0 22 22"><path d="M3 5h7v13H3zM12 5h7v13h-7z" fill="none" stroke="#888" stroke-width="1.2"/></svg>
      <span>Manager Guides</span>
    </div>
    <div class="service-card">
      <svg width="22" height="22" viewBox="0 0 22 22"><rect x="5" y="3" width="12" height="16" fill="none" stroke="#888" stroke-width="1.2"/><path d="M8 9l2 2 4-4" stroke="#888" fill="none"/></svg>
      <span>Policy Manuals</span>
    </div>
    <div class="service-card">
      <svg width="22" height="22" viewBox="0 0 22 22"><circle cx="11" cy="11" r="6" fill="none" stroke="#888" stroke-width="1.2"/><circle cx="11" cy="11" r="2" fill="#888"/></svg>
      <span>Operations Manuals</span>
    </div>
    <div class="service-card">
      <svg width="22" height="22" viewBox="0 0 22 22"><path d="M4 11l7-6 7 6v7H4z" fill="none" stroke="#888" stroke-width="1.2"/></svg>
      <span>Property Management Manuals</span>
    </div>
    <div class="service-card">
      <svg width="22" height="22" viewBox="0 0 22 22"><rect x="3" y="4" width="16" height="11" fill="none" stroke="#888" stroke-width="1.2"/><path d="M11 15v4M7 19h8" stroke="#888"/></svg>
      <span>Orientation Programs &amp; Presentations</span>
    </div>
    <div class="service-card">
      <svg width="22" height="22" viewBox="0 0 22 22"><path d="M4 18V12M9 18V8M14 18V10M19 18V5" stroke="#888" stroke-width="2"/></svg>
      <span>Performance Management Prog &amp; Communications</span>
    </div>
    <div class="service-card">
      <svg width="22" height="22" viewBox="0 0 22 22"><path d="M11 18s-7-4-7-9a3.5 3.5 0 0 1 7-1 3.5 3.5 0 0 1 7 1c0 5-7 9-7 9z" fill="none" stroke="#888" stroke-width="1.2"/></svg>
      <span>Benefits Communications</span>
    </div>
  </div>
</section>

<section class="testimonials">
  <div class="testimonial-photo" role="img" aria-label="Single tulip in soft focus against a dark background"></div>
  <h2 class="section-title">CLIENT TESTIMONIALS</h2>
  <div class="quote-slider">
    <div class="slide-arrow"><svg width="8" height="8" viewBox="0 0 8 8"><path d="M5.5 1L2.5 4l3 3" stroke="#333" fill="none" stroke-width="1.3"/></svg></div>
    <div class="client-badge">KESTREL</div>
    <div class="slide-arrow"><svg width="8" height="8" viewBox="0 0 8 8"><path d="M2.5 1l3 3-3 3" stroke="#333" fill="none" stroke-width="1.3"/></svg></div>
  </div>
  <div class="quote-author">
    <strong>Dale Morrow</strong>
    <em>Director of Kestrel Office</em>
  </div>
  <p class="quote-text"><b>“Brightwave Counsel forges long-term relationships.”</b><br>
  Kestrel Office has turned to Brightwave Counsel on many occasions over the last seven years for guidance in developing our management and leadership learning curriculum, as well as consulting on a number of high-impact human resource projects.</p>
</section>

<section class="client-strip">
  <svg class="edge left" width="10" height="16" viewBox="0 0 10 16"><path d="M8 1L2 8l6 7" stroke="#999" fill="none" stroke-width="1.5"/></svg>
  <span class="client-name">Hollisgate</span>
  <span class="client-name">Brookvale</span>
  <span class="client-name">Cedarline Homes</span>
  <span class="client-name">Marlow &amp; Finch</span>
  <span class="client-name">Paylark</span>
  <svg class="edge right" width="10" height="16" viewBox="0 0 10 16"><path d="M2 1l6 7-6 7" stroke="#999" fill="none" stroke-width="1.5"/></svg>
</section>

<footer class="site-footer">
  <h3>CONTACT US</h3>
  <div class="contact-row">
    <div class="contact-item address">
      <svg width="12" height="14" viewBox="0 0 12 14"><path d="M6 13S1.5 8 1.5 5a4.5 4.5 0 0 1 9 0C10.5 8 6 13 6 13z" fill="#ccc"/><circle cx="6" cy="5" r="1.6" fill="#2c2c2c"/></svg>
      <div><strong>Address</strong>240 Orchard Lane, Suite 5<br>Alder Springs, GA 30000</div>
    </div>
    <div class="contact-item phone">
      <svg width="12" height="14" viewBox="0 0 12 14"><rect x="3" y="1" width="6" height="12" rx="1" fill="none" stroke="#ccc" stroke-width="1.2"/><circle cx="6" cy="11" r=".8" fill="#ccc"/></svg>
      <div><strong>Phone</strong>(555) 014-2290</div>
    </div>
    <div class="contact-item email">
      <svg width="14" height="12" viewBox="0 0 14 12"><rect x="1" y="2" width="12" height="8" fill="none" stroke="#ccc" stroke-width="1.2"/><path d="M1 2l6 5 6-5" stroke="#ccc" fill="none"/></svg>
      <div><strong>Email</strong>info@brightwavecounsel-example.com</div>
    </div>
    <div class="social"><i></i>ProLinker</div>
  </div>
  <div class="footer-bar">
    <nav><a href="#">Home</a><a href="#">What We Do</a><a href="#">Who We Are</a><a href="#">Our Clients</a><a href="#">Snapshots</a></nav>
    <span>© 2024 Brightwave Counsel. All Rights Reserved.</span>
  </div>
</footer>

</body>
</html>
```